Business Card for Pottery and Jewellery Designer

A new business card design is needed to accompany a newly launching pottery and jewellery website. The company logo has been attached for use. The company is called Kilnwick Lane. For a sense of the vibe please see the website (it is currently under construction but this way you'll get a feel for the style) www.KilnwickLane.com

The website font is Pontano Sans for the body of the text with Overlock for headers.

The overall look should be clean and elegant. The back side can have just the logo. The front side should have a smaller logo and the following details displayed:

Kilnwick Lane
Designer: Marisol Bexley
Phone: xxx.xxx.xxxx
Email: Designer@KilnwickLane.com

The structure of displaying this is completely up to you. Different layouts and creative methods of displaying contact info are welcome as long as it stays clean/uncluttered.

No product photographs are to be included in the design as the catalogue changes quickly.

Colour preferences lean towards elegant and understated (charcoal grey, dark navy blue etc.)

Please let me know if you have any further questions or further details required.

Target Market(s)

Target market is 30+ year old women

Industry/Entity Type

Construction

Colors
ffffff
1b1b1b
474747
d9d9d9
fafafa
0355a3

Requirements
Must have
• The submissions so far have looked very typical and don't stand out right now. They're also all in navy with very little variation. I'm looking for something that stands out a it more while still being clean-looking.
Nice to have
• I've attached a few design samples and an idea for a backdrop. It would be great to see some designs in black, white, and grey with only a hint of color.
Should not have
• Product Images

```html
<!DOCTYPE html>
<html lang="en">
<head>
<meta charset="utf-8">
<title>Kilnwick Lane – Business Card</title>
<link rel="stylesheet" href="https://fonts.googleapis.com/css2?family=Tinos&display=swap">
<style>
  :root {
    --backdrop: #0a2148;
    --card: #c7e3f6;
    --ink: #0b5aa6;
    --clay: #d98f4e;
    --stone: #d8cfb8;
    --shadow: rgba(0, 0, 0, 0.45);
  }
  * { box-sizing: border-box; margin: 0; padding: 0; }
  html, body {
    width: 1200px;
    height: 1000px;
    overflow: hidden;
    background: var(--backdrop);
  }
  .canvas {
    position: relative;
    width: 1200px;
    height: 1000px;
    font-family: "Tinos", "Times New Roman", serif;
    color: var(--ink);
  }
  .card {
    position: absolute;
    background: var(--card);
    box-shadow: 6px 8px 14px var(--shadow);
  }
  .card--front { left: 40px; top: 50px; width: 790px; height: 470px; }
  .card--back  { left: 360px; top: 530px; width: 790px; height: 430px; }

  .front__name {
    position: absolute;
    left: 0; right: 0; top: 58px;
    text-align: center;
    font-size: 50px;
    transform: translateX(-20px);
  }
  .front__role, .front__person {
    position: absolute;
    left: 0; right: 0;
    text-align: center;
    font-size: 32px;
    transform: translateX(-20px);
  }
  .front__role { top: 150px; }
  .front__person { top: 200px; }

  .front__contact {
    position: absolute;
    left: 300px; top: 392px;
    font-size: 21px;
    line-height: 30px;
  }

  .artwork {
    position: absolute;
    border-radius: 18px 18px 28px 28px;
    background: linear-gradient(100deg, var(--clay) 0%, var(--clay) 45%, var(--stone) 55%, var(--stone) 100%);
    box-shadow: 3px 5px 8px rgba(0, 0, 0, 0.25);
  }
  .artwork--left  { left: 80px;  top: 330px; width: 180px; height: 140px; }
  .artwork--right { left: 530px; top: 250px; width: 170px; height: 95px;
    background: linear-gradient(100deg, var(--stone) 0%, var(--stone) 40%, var(--clay) 55%, var(--clay) 100%); }

  .back__name {
    position: absolute;
    left: 100px; top: 100px;
    font-size: 64px;
    letter-spacing: 2px;
  }
  .back__rule {
    position: absolute;
    left: 90px; top: 196px;
    width: 530px; height: 1px;
    background: var(--ink);
  }
</style>
</head>
<body>
  <main class="canvas">
    <section class="card card--front" aria-label="Business card front">
      <h1 class="front__name">Kilnwick Lane</h1>
      <p class="front__role">Designer:</p>
      <p class="front__person">Marisol Bexley</p>
      <div class="artwork artwork--left" role="img" aria-label="Illustration of clay pots and a stoneware jar"></div>
      <div class="artwork artwork--right" role="img" aria-label="Illustration of a stoneware cup and a clay bowl"></div>
      <address class="front__contact" style="font-style: normal;">
        <div>Phone: xxx.xxx.xxxx</div>
        <div>Email: Designer@KilnwickLane.com</div>
      </address>
    </section>

    <section class="card card--back" aria-label="Business card back">
      <h2 class="back__name">Kilnwick Lane</h2>
      <div class="back__rule"></div>
    </section>
  </main>
</body>
</html>
```